Quilvo Garage Doors Business Card

I need a Business Card for my garage door business:
Quilvo Garage Doors.
please add:
logo
phone number: 855-3-QUILVO
(853-392)

email: service@quilvogaragedoors.com
website: www.quilvogaragedoors.com

The attached image is recommendation ONLY.

```html
<!DOCTYPE html>
<html lang="en">
<head>
<meta charset="utf-8">
<title>Quilvo Garage Doors – Business Card</title>
<link rel="stylesheet" href="https://fonts.googleapis.com/css2?family=Quicksand:wght@500;700&display=swap">
<style>
  :root {
    --page: #ebe6df;
    --card: #ffffff;
    --ink: #141414;
    --teal: #2a98a8;
    --teal-deep: #1d7f90;
    --teal-soft: #8fcfd8;
    --teal-pale: #d3ebef;
    --teal-band: #45bccb;
  }
  * { margin: 0; padding: 0; box-sizing: border-box; }
  html, body { width: 1200px; height: 720px; overflow: hidden; }
  body {
    background: var(--page);
    font-family: "Quicksand", sans-serif;
    position: relative;
  }
  .card {
    position: absolute;
    top: 205px;
    width: 540px;
    height: 309px;
    background: var(--card);
    overflow: hidden;
    box-shadow: 0 6px 18px rgba(0,0,0,.12);
  }
  .card--front { left: 40px; }
  .card--back { left: 620px; }
  .card__shapes { position: absolute; inset: 0; }

  .brand { position: absolute; display: flex; align-items: center; gap: 14px; }
  .brand__mark { background: var(--teal); flex: none; }
  .brand__name {
    font-weight: 700;
    color: var(--ink);
    line-height: 1.05;
  }
  .card--front .brand { left: 168px; top: 112px; }
  .card--front .brand__mark { width: 46px; height: 46px; }
  .card--front .brand__name { font-size: 31px; }

  .card--back .brand { left: 38px; top: 34px; }
  .card--back .brand__mark { width: 38px; height: 38px; }
  .card--back .brand__name { font-size: 24px; }

  .contact {
    position: absolute;
    left: 40px;
    top: 128px;
    list-style: none;
    color: var(--teal);
    font-size: 14px;
    font-weight: 500;
    line-height: 1.35;
  }
  .contact li { display: flex; align-items: flex-start; gap: 10px; margin-bottom: 10px; }
  .contact svg { flex: none; margin-top: 2px; }

  .web-band {
    position: absolute;
    left: 0;
    top: 246px;
    width: 350px;
    height: 32px;
    background: var(--teal-band);
    color: #fff;
    font-weight: 700;
    font-size: 15px;
    display: flex;
    align-items: center;
    padding-left: 40px;
    letter-spacing: .2px;
  }
</style>
</head>
<body>

<section class="card card--front" aria-label="Business card front">
  <svg class="card__shapes" viewBox="0 0 540 309" aria-hidden="true">
    <polygon points="0,40 90,0 140,0 140,240 0,309" fill="var(--teal-pale)"/>
    <polygon points="0,120 110,70 110,309 0,309" fill="var(--teal)" opacity=".85"/>
    <polygon points="0,200 60,170 60,309 0,309" fill="var(--teal-deep)" opacity=".6"/>
    <polygon points="70,220 230,220 270,309 40,309" fill="var(--teal)" opacity=".8"/>
    <polygon points="230,220 290,309 250,309" fill="var(--teal-soft)"/>
    <polygon points="470,0 540,0 540,100 440,120" fill="var(--teal-pale)"/>
    <polygon points="410,120 540,60 540,309 420,309" fill="var(--teal)" opacity=".9"/>
    <polygon points="470,180 540,150 540,309 480,309" fill="var(--teal-deep)" opacity=".5"/>
  </svg>
  <div class="brand">
    <span class="brand__mark"></span>
    <p class="brand__name">Quilvo<br>Garage Doors</p>
  </div>
</section>

<section class="card card--back" aria-label="Business card back">
  <svg class="card__shapes" viewBox="0 0 540 309" aria-hidden="true">
    <polygon points="490,40 540,10 540,120 470,140" fill="var(--teal-pale)"/>
    <polygon points="430,150 540,110 540,309 450,309" fill="var(--teal)" opacity=".9"/>
    <polygon points="490,200 540,180 540,309 500,309" fill="var(--teal-deep)" opacity=".5"/>
  </svg>
  <div class="brand">
    <span class="brand__mark"></span>
    <p class="brand__name">Quilvo<br>Garage Doors</p>
  </div>
  <ul class="contact">
    <li>
      <svg width="13" height="13" viewBox="0 0 24 24" aria-hidden="true"><path fill="var(--teal)" d="M6.6 10.8a15.1 15.1 0 0 0 6.6 6.6l2.2-2.2a1 1 0 0 1 1-.25 11.4 11.4 0 0 0 3.6.57 1 1 0 0 1 1 1V20a1 1 0 0 1-1 1A17 17 0 0 1 3 4a1 1 0 0 1 1-1h3.5a1 1 0 0 1 1 1c0 1.25.2 2.45.57 3.6a1 1 0 0 1-.25 1z"/></svg>
      <span>855-3-QUILVO<br>(853-392)</span>
    </li>
    <li>
      <svg width="13" height="13" viewBox="0 0 24 24" aria-hidden="true"><rect x="2" y="5" width="20" height="14" rx="1" fill="none" stroke="var(--teal)" stroke-width="2"/><path d="M2 6l10 7 10-7" fill="none" stroke="var(--teal)" stroke-width="2"/></svg>
      <span>service@quilvogaragedoors.com</span>
    </li>
  </ul>
  <div class="web-band">www.quilvogaragedoors.com</div>
</section>

</body>
</html>
```